Rack Card for Portuguese Walking Food Tour

I would like a vertical rack card measuring 99x210mm. Here is the information I would like to include. It does not need to be in this format. We are located in Setubal, Portugal.
Please use the attached Teal Heron Logo.
Setúbal: Tradition and Today
Experience the culinary delights of Setúbal, Portugal with a walking food tour around our waterfront village. Discover the Mercado da Gaivota Branca, voted one of the world’s best markets by Metro Ledger, and indulge in local wines and dishes. Prepare for a calm stroll on flat streets. No hills to climb on this tour.
Duration: 4 hours
www.brinebasketwalks.com
+351 265 000 487

```html
<!DOCTYPE html>
<html lang="en">
<head>
<meta charset="utf-8">
<title>Setúbal Walking Food Tour – Rack Card</title>
<link rel="stylesheet" href="https://fonts.googleapis.com/css2?family=Kaushan+Script&family=Poppins:wght@600;700;800&family=Fira+Sans+Condensed:ital,wght@1,500&display=swap">
<style>
  :root{
    --orange:#f26522;
    --purple:#9e3d86;
    --paper:#f1f1f1;
    --ink:#000000;
    --white:#ffffff;
    --page:#ffffff;
  }
  *{box-sizing:border-box;margin:0;padding:0}
  html,body{width:1200px;height:1000px;overflow:hidden;background:var(--page)}
  .rack-card{position:absolute;left:395px;top:68px;width:410px;height:862px;overflow:hidden;background:var(--paper)}
  .card-art{position:absolute;inset:0}
  .brand{position:absolute;left:0;top:0;width:190px;height:75px;background:var(--ink);border-bottom-right-radius:38px;display:flex;align-items:center;gap:9px;padding-left:18px}
  .brand-dot{width:22px;height:22px;border-radius:50%;background:var(--orange);flex:none}
  .brand-name{font-family:"Poppins",sans-serif;font-weight:600;font-size:14px;color:var(--orange);line-height:1.1}
  .title{position:absolute;text-align:center;margin:0}
  .title-main{left:0;width:370px;top:142px;font-family:"Kaushan Script",cursive;font-weight:400;font-size:84px;line-height:1;color:var(--orange);
    text-shadow:2px 0 0 var(--white),-2px 0 0 var(--white),0 2px 0 var(--white),0 -2px 0 var(--white),2px 2px 0 var(--white),-2px -2px 0 var(--white),2px -2px 0 var(--white),-2px 2px 0 var(--white),5px 5px 0 var(--ink)}
  .title-sub{left:0;width:350px;top:248px;font-family:"Poppins",sans-serif;font-weight:800;font-size:24px;line-height:1.2;color:var(--white);
    text-shadow:1.5px 0 0 var(--ink),-1.5px 0 0 var(--ink),0 1.5px 0 var(--ink),0 -1.5px 0 var(--ink),1.5px 1.5px 0 var(--ink),-1.5px -1.5px 0 var(--ink),1.5px -1.5px 0 var(--ink),-1.5px 1.5px 0 var(--ink),3px 3px 0 var(--ink)}
  .intro{position:absolute;left:24px;top:318px;width:250px;font-family:"Fira Sans Condensed",sans-serif;font-style:italic;font-weight:500;font-size:12.3px;line-height:19px;color:var(--white)}
  .duration{position:absolute;left:30px;top:670px}
  .duration-label{display:flex;align-items:center;gap:6px;font-family:"Poppins",sans-serif;font-weight:700;font-size:22px;line-height:1.2;color:var(--white)}
  .duration-value{margin-top:4px;width:185px;height:62px;background:var(--ink);clip-path:polygon(3% 10%,96% 0,100% 45%,94% 100%,6% 92%,0 52%);display:flex;align-items:center;justify-content:center;font-family:"Kaushan Script",cursive;font-size:36px;color:var(--white)}
  .contact{position:absolute;left:0;top:777px;width:410px;height:85px;background:var(--ink);text-align:center;font-family:"Poppins",sans-serif;font-weight:700;font-size:21px;line-height:34px;color:var(--orange);padding-top:8px}
</style>
</head>
<body>
<main class="rack-card">
  <svg class="card-art" viewBox="0 0 410 862" width="410" height="862">
    <defs>
      <linearGradient id="town-tone" x1="0" y1="0" x2="1" y2="1">
        <stop offset="0" stop-color="#7d7a80"/>
        <stop offset="0.35" stop-color="#b0447f"/>
        <stop offset="0.7" stop-color="#4f4a52"/>
        <stop offset="1" stop-color="#6f7a5a"/>
      </linearGradient>
      <radialGradient id="wine-tone" cx="0.45" cy="0.4" r="0.7">
        <stop offset="0" stop-color="#c9c3b6"/>
        <stop offset="0.55" stop-color="#7a6452"/>
        <stop offset="1" stop-color="#3e3129"/>
      </radialGradient>
      <radialGradient id="oyster-tone" cx="0.45" cy="0.45" r="0.7">
        <stop offset="0" stop-color="#eef1f2"/>
        <stop offset="0.45" stop-color="#b6bcc0"/>
        <stop offset="0.8" stop-color="#7f8a85"/>
        <stop offset="1" stop-color="#d9dde0"/>
      </radialGradient>
      <radialGradient id="board-tone" cx="0.45" cy="0.4" r="0.7">
        <stop offset="0" stop-color="#e8cf9e"/>
        <stop offset="0.5" stop-color="#c58d55"/>
        <stop offset="0.85" stop-color="#7a4a3c"/>
        <stop offset="1" stop-color="#5a3a30"/>
      </radialGradient>
      <radialGradient id="fish-tone" cx="0.5" cy="0.5" r="0.7">
        <stop offset="0" stop-color="#f2b59a"/>
        <stop offset="0.5" stop-color="#df7a5c"/>
        <stop offset="1" stop-color="#b8503e"/>
      </radialGradient>
    </defs>

    <rect class="photo-town" x="0" y="0" width="410" height="330" fill="url(#town-tone)" role="img" aria-label="Photo of the large Setúbal town sign with a pink heart sculpture"/>
    <path d="M8,225 C40,290 170,300 260,285 C340,272 400,220 404,150 C406,80 370,30 330,5" fill="none" stroke="var(--white)" stroke-width="5" stroke-linecap="round"/>

    <path class="band-orange" d="M0,252 C130,238 300,255 410,262 L410,300 C402,430 350,540 250,590 C170,628 90,630 0,634 Z" fill="var(--orange)"/>
    <path class="band-purple" d="M0,252 C130,238 300,255 410,262 L398,300 C390,420 335,520 240,570 C165,608 85,612 0,614 Z" fill="var(--purple)"/>
    <rect class="block-orange" x="0" y="622" width="250" height="155" fill="var(--orange)"/>

    <circle cx="355" cy="379" r="45" fill="url(#wine-tone)" stroke="var(--white)" stroke-width="4" role="img" aria-label="Photo of glasses of local wine at a bar"/>
    <circle cx="280" cy="512" r="84" fill="url(#oyster-tone)" stroke="var(--white)" stroke-width="4" role="img" aria-label="Photo of fresh oysters on ice with lemon"/>
    <circle cx="95" cy="577" r="92" fill="url(#board-tone)" stroke="var(--white)" stroke-width="4" role="img" aria-label="Photo of a board with toasted bread, chouriço and cheese"/>
    <circle cx="345" cy="670" r="110" fill="url(#fish-tone)" stroke="var(--white)" stroke-width="4" role="img" aria-label="Photo of fresh red mullet at the fish market"/>
  </svg>

  <div class="brand">
    <span class="brand-dot"></span>
    <span class="brand-name">Teal Heron Tours</span>
  </div>

  <h1 class="title title-main">Setúbal</h1>
  <p class="title title-sub">Tradition and Today</p>

  <p class="intro">Experience the culinary delights of Setúbal, Portugal with a walking food tour around our waterfront village. Discover the Mercado da Gaivota Branca, voted one of the world’s best markets by Metro Ledger, and indulge in local wines and dishes. Prepare for a calm stroll on flat streets. No hills to climb on this tour.</p>

  <div class="duration">
    <p class="duration-label">
      <svg width="20" height="20" viewBox="0 0 20 20" aria-hidden="true"><circle cx="10" cy="10" r="8" fill="none" stroke="var(--white)" stroke-width="2.5"/><path d="M10 5v5l3 2" fill="none" stroke="var(--white)" stroke-width="2.2" stroke-linecap="round"/></svg>
      Duration
    </p>
    <p class="duration-value">4 hours</p>
  </div>

  <footer class="contact">
    <p>www.brinebasketwalks.com</p>
    <p>+351 265 000 487</p>
  </footer>
</main>
</body>
</html>
```